Business Card Design for a technology company

Our current business card is outdated and stale.

We need a new look and one soon.

We're a telematics (GPS tracking) company based in Australia. Our audiences are transport and logistics company.

Target Market(s)

1. Transport and Logistics Companies
2. Food and Beverage Manufacturers
3. Concrete Businesses

Industry/Entity Type

Logistics

Contact Information for Business Card

Halvor Pinet

Font styles to use
Sans Serif

Colors
3276b5
0255a3
85acd3
cfdeed
ffffff

Requirements
Must have
• Logo
• "Premium Suppliers of Real Time Temperature Tracking"
• Contact Name
• Business Title
• Address
• Telephone
• Mobile
• Email
• Website URL
Nice to have
• Visual representation of tracking or maps.
Should not have
• Image of a satellite as currently shown

```html
<!DOCTYPE html>
<html lang="en">
<head>
<meta charset="utf-8">
<title>Halvor Pinet – Business Card</title>
<link href="https://fonts.googleapis.com/css2?family=Barlow+Condensed:wght@400;500;600&display=swap" rel="stylesheet">
<style>
  :root {
    --bg: #d3d4d6;
    --front-top: #6a97cc;
    --front-bottom: #1f4590;
    --white: #ffffff;
    --brand: #0255a3;
    --ink: #222222;
    --divider: #cfcfcf;
    --icon: #23408e;
  }
  * { margin: 0; padding: 0; box-sizing: border-box; }
  html, body {
    width: 975px; height: 1200px; overflow: hidden;
    background: var(--bg);
    font-family: "Barlow Condensed", "Arial Narrow", sans-serif;
  }
  .canvas { position: relative; width: 975px; height: 1200px; }
  .card {
    position: absolute; left: 128px; width: 720px; height: 440px;
    border-radius: 26px; overflow: hidden;
    box-shadow: 0 4px 14px rgba(0,0,0,0.18);
  }
  .card-front {
    top: 128px;
    background: linear-gradient(180deg, var(--front-top) 0%, var(--front-bottom) 100%);
  }
  .front-brand {
    position: absolute; left: 0; right: 0; top: 268px;
    text-align: center; color: var(--white);
    font-weight: 600; font-size: 96px; line-height: 1; letter-spacing: 0.5px;
  }
  .tagline {
    position: absolute; left: 0; right: 0; top: 354px;
    display: flex; justify-content: center; align-items: center; gap: 12px;
    color: var(--white); font-weight: 600; font-size: 26px;
  }
  .tagline svg { width: 22px; height: 28px; fill: var(--white); }
  .tagline-rule {
    position: absolute; left: 53px; right: 53px; top: 395px;
    border-top: 2px dashed rgba(255,255,255,0.9);
  }
  .card-back { top: 632px; background: var(--white); }
  .back-brand {
    position: absolute; left: 42px; top: 193px; width: 330px;
    display: flex; align-items: center; gap: 10px;
    color: var(--brand); font-weight: 600; font-size: 52px; line-height: 1;
  }
  .back-brand .mark { width: 18px; height: 18px; border-radius: 50%; background: var(--brand); flex: none; }
  .divider {
    position: absolute; left: 356px; top: 57px; height: 325px;
    border-left: 2px solid var(--divider);
  }
  .contact { position: absolute; left: 384px; top: 96px; color: var(--ink); }
  .contact-name { font-weight: 600; font-size: 26px; line-height: 1.05; letter-spacing: 0.3px; }
  .contact-title { font-weight: 400; font-size: 21px; line-height: 1.2; }
  .contact-address { margin-top: 16px; font-size: 21px; line-height: 28px; }
  .contact-list { list-style: none; margin-top: 14px; font-size: 21px; line-height: 27.5px; }
  .contact-list li { display: flex; align-items: center; gap: 5px; }
  .contact-list svg { width: 15px; height: 15px; fill: var(--icon); flex: none; }
</style>
</head>
<body>
<main class="canvas">
  <section class="card card-front" aria-label="Card front">
    <div class="front-brand">Halvor Pinet</div>
    <p class="tagline">
      <svg viewBox="0 0 24 32" aria-hidden="true"><path d="M12 0C5.4 0 0 5.3 0 11.9 0 20.8 12 32 12 32s12-11.2 12-20.1C24 5.3 18.6 0 12 0zm0 17a5 5 0 1 1 0-10 5 5 0 0 1 0 10z"/></svg>
      Premium Suppliers of Real Time Temperature Tracking
      <svg viewBox="0 0 24 32" aria-hidden="true"><path d="M12 0C5.4 0 0 5.3 0 11.9 0 20.8 12 32 12 32s12-11.2 12-20.1C24 5.3 18.6 0 12 0zm0 17a5 5 0 1 1 0-10 5 5 0 0 1 0 10z"/></svg>
    </p>
    <div class="tagline-rule"></div>
  </section>

  <section class="card card-back" aria-label="Card back">
    <div class="back-brand"><span class="mark"></span>Halvor Pinet</div>
    <div class="divider"></div>
    <div class="contact">
      <p class="contact-name">DORIAN KESSEL</p>
      <p class="contact-title">CEO</p>
      <p class="contact-address">4, 18 Marlow Street<br>Ferndale VIC 3190</p>
      <ul class="contact-list">
        <li><svg viewBox="0 0 16 16" aria-hidden="true"><path d="M3.6 1l2.3 2.9-1.3 1.9c.9 2 2.6 3.7 4.6 4.6l1.9-1.3L14 11.4 12.6 14C6.6 13.6 2.4 9.4 2 3.4z"/></svg>+61 3 9000 1234</li>
        <li><svg viewBox="0 0 16 16" aria-hidden="true"><path d="M4 0h8a1.5 1.5 0 0 1 1.5 1.5v13A1.5 1.5 0 0 1 12 16H4a1.5 1.5 0 0 1-1.5-1.5v-13A1.5 1.5 0 0 1 4 0zm0 2v10.5h8V2zm4 11.3a.9.9 0 1 0 0 1.8.9.9 0 0 0 0-1.8z"/></svg>+61 3 9000 1234</li>
        <li><svg viewBox="0 0 16 16" aria-hidden="true"><path d="M0 3h16v1.2L8 9 0 4.2zm0 2.6l8 4.8 8-4.8V13H0z"/></svg>dkessel@HalvorPinet.com.au</li>
        <li><svg viewBox="0 0 16 16" aria-hidden="true"><path d="M8 0a8 8 0 1 0 0 16A8 8 0 0 0 8 0zm5.9 7.2h-2.6a12 12 0 0 0-.9-4.6 6.5 6.5 0 0 1 3.5 4.6zM8 1.6c.8 1 1.6 3 1.7 5.6H6.3C6.4 4.6 7.2 2.6 8 1.6zM5.6 2.6a12 12 0 0 0-.9 4.6H2.1a6.5 6.5 0 0 1 3.5-4.6zM2.1 8.8h2.6c.1 1.8.4 3.3.9 4.6a6.5 6.5 0 0 1-3.5-4.6zM8 14.4c-.8-1-1.6-3-1.7-5.6h3.4c-.1 2.6-.9 4.6-1.7 5.6zm2.4-1c.5-1.3.8-2.8.9-4.6h2.6a6.5 6.5 0 0 1-3.5 4.6z"/></svg>www.HalvorPinet.com.au</li>
      </ul>
    </div>
  </section>
</main>
</body>
</html>
```